Willowmere Spa and Beauty Ltd. (Name of business)

I need a business card designed for this new company based out of Toronto Ontario. We specialize in Eyelash Extensions, Manicures and Pedicures, body waxing, massages, laser hair removal and botox treatments. Also offer a variety of products for sale, such as skin cream serums, collagen gel, eye cream, etc. It is a safe relaxing and non-judgemental environnment. Clients are welcome to come be pampered for the half or full day. Many service packages to choose from.

Open 7days per week from 8am to 8pm.

Priscilla Dunmore
Spa Facilitator
Willowmere Spa and Beauty Ltd.
7200 Harcourt St; Suite 1400
Toronto ON K2P 9W4

OFFICE: 416.790.4100
FAX: 416.790.4101
CELL: 416.632.1987
EMAIL: priscilla.dunmore@willowmerespa.com

Target Market(s)

Target market is primarily female ranging from 16 years old to 50 years old.

Industry/Entity Type

Business

Contact Information for Business Card

Priscilla Dunmore
Spa Facilitator
7200 Harcourt St; Suite 1400
Toronto ON K2P 9W4

OFFICE: 416.790.4100
FAX: 416.790.4101
CELL: 416.632.1987

Logo Text

I dont have a logo yet. I would like it simple but sophisticated and modern.

Font styles to use
Serif

Requirements
Must have
• all pertinent details such as company name, logo, name and contact information, services that are offered, including package rates
Nice to have
• Company name and logo prominent. A card that is neat and the information such as address, phone number, fax, email, etc is not too crowded but laid out in an easy to read format.
• Possibly on the back of card - some of the services offered could be listed, as well as professional cream lotions and serums. Hours of operation etc.

```html
<!DOCTYPE html>
<html lang="en">
<head>
<meta charset="utf-8">
<title>Willowmere Spa and Beauty Ltd. — Business Card</title>
<link rel="stylesheet" href="https://fonts.googleapis.com/css2?family=Barlow:ital,wght@0,500;0,600;0,700;1,500&display=swap">
<style>
  :root {
    --page-bg: #ece7e1;
    --card-white: #ffffff;
    --rose: #e2647e;
    --rose-deep: #c9405c;
    --teal: #52c6bf;
    --teal-text: #3db5ad;
    --petal-light: #f7b9c4;
    --petal-mid: #f08ca0;
    --petal-coral: #f07a6a;
    --skin-light: #f3d6c6;
    --hair-tone: #d9b58c;
  }
  * { margin: 0; padding: 0; box-sizing: border-box; }
  html, body { width: 980px; height: 1200px; overflow: hidden; }
  body {
    background: var(--page-bg);
    font-family: "Barlow", "Helvetica Neue", Arial, sans-serif;
    position: relative;
  }
  .card {
    position: absolute;
    background: var(--card-white);
    overflow: hidden;
  }
  .card svg.card-art { position: absolute; inset: 0; width: 100%; height: 100%; }

  /* Back of card */
  .card-back { left: 105px; top: 178px; width: 689px; height: 393px; }
  .brand {
    position: absolute; left: 0; right: 0; top: 98px;
    display: flex; justify-content: center; align-items: center; gap: 10px;
    color: var(--teal); font-weight: 600; font-size: 30px; letter-spacing: 1px;
  }
  .brand-dot { width: 14px; height: 14px; border-radius: 50%; background: var(--teal); }
  .address {
    position: absolute; left: 0; right: 0; top: 181px;
    text-align: center; color: var(--rose); font-weight: 500;
    font-size: 18px; line-height: 25px;
  }
  .hours {
    position: absolute; left: 0; right: 0; top: 263px;
    text-align: center; color: var(--rose-deep); font-weight: 600; font-size: 18px;
  }
  .services {
    position: absolute; left: 60px; right: 60px; top: 299px;
    text-align: center; color: var(--teal-text); font-weight: 600;
    font-size: 13.5px; line-height: 20px; text-transform: uppercase; letter-spacing: 0.3px;
  }

  /* Front of card */
  .card-front { left: 181px; top: 620px; width: 691px; height: 399px; }
  .person-name {
    position: absolute; left: 52px; top: 64px;
    color: var(--rose-deep); font-weight: 700; font-size: 35px;
    letter-spacing: 0.5px; text-transform: uppercase;
  }
  .person-title {
    position: absolute; left: 92px; top: 110px;
    color: var(--teal-text); font-weight: 500; font-style: italic;
    font-size: 23px; letter-spacing: 3px; text-transform: uppercase;
  }
  .contact-list {
    position: absolute; left: 56px; top: 185px; list-style: none;
    color: var(--rose); font-weight: 500; font-size: 17px; line-height: 24px;
  }
</style>
</head>
<body>

<section class="card card-back" aria-label="Card back">
  <svg class="card-art" viewBox="0 0 689 393" preserveAspectRatio="none" aria-hidden="true">
    <defs>
      <linearGradient id="petalWashBack" x1="0" y1="0" x2="1" y2="0">
        <stop offset="0" stop-color="#f6a9b8"/>
        <stop offset="0.5" stop-color="#f2a0b2"/>
        <stop offset="0.8" stop-color="#f48a7a"/>
        <stop offset="1" stop-color="#ef9aa8"/>
      </linearGradient>
    </defs>
    <rect width="689" height="180" fill="url(#petalWashBack)"/>
    <path d="M0 175 Q344 -10 689 175 L689 393 L0 393 Z" fill="#ffffff"/>
    <path d="M0 172 Q344 -14 689 172" fill="none" stroke="#52c6bf" stroke-width="5"/>
    <path d="M0 340 Q344 372 689 340 L689 393 L0 393 Z" fill="#52c6bf"/>
  </svg>
  <div role="img" aria-label="Soft pink and coral floral artwork across the top band" style="position:absolute;left:0;top:0;width:689px;height:60px;"></div>

  <div class="brand"><span class="brand-dot"></span>Willowmere</div>
  <p class="address">Willowmere Spa and Beauty Ltd.<br>7200 Harcourt St; Suite 1400<br>Toronto ON K2P 9W4</p>
  <p class="hours">Open 7days per week from 8am to 8pm</p>
  <p class="services">We specialize in eyelash extensions, manicures and pedicures, body waxing, massages, laser hair removal and botox treatments.</p>
</section>

<section class="card card-front" aria-label="Card front">
  <svg class="card-art" viewBox="0 0 691 399" preserveAspectRatio="none" aria-hidden="true">
    <defs>
      <linearGradient id="petalWashFront" x1="0" y1="0" x2="0" y2="1">
        <stop offset="0" stop-color="#f6b3c0"/>
        <stop offset="0.6" stop-color="#f08ca0"/>
        <stop offset="1" stop-color="#ec7b8a"/>
      </linearGradient>
      <linearGradient id="portraitWash" x1="0" y1="0" x2="1" y2="1">
        <stop offset="0" stop-color="#dcb78e"/>
        <stop offset="0.5" stop-color="#f1d3c1"/>
        <stop offset="1" stop-color="#e8bfa8"/>
      </linearGradient>
    </defs>
    <path d="M435 0 Q478 40 480 140 L480 399 L691 399 L691 0 Z" fill="url(#petalWashFront)"/>
    <path d="M435 0 Q478 40 480 140 L480 399" fill="none" stroke="#52c6bf" stroke-width="4"/>
    <path d="M0 335 Q345 375 691 335 L691 399 L0 399 Z" fill="#52c6bf"/>
  </svg>
  <div role="img" aria-label="Portrait photograph of a smiling woman with a white lily in her hair"
       style="position:absolute;left:415px;top:55px;width:250px;height:344px;border-radius:120px 120px 0 0;background:linear-gradient(160deg,var(--hair-tone),var(--skin-light) 55%,#e9c2ac);"></div>

  <h1 class="person-name">Priscilla Dunmore</h1>
  <p class="person-title">Spa Facilitator</p>
  <ul class="contact-list">
    <li>OFFICE: 416.790.4100</li>
    <li>FAX: 416.790.4101</li>
    <li>CELL: 416.632.1987</li>
    <li>EMAIL: priscilla.dunmore@willowmerespa.com</li>
  </ul>
</section>

</body>
</html>
```